依頼詳細
シンプルかつスタイリッシュで、落ち着いたデザインを希望します。弊社イメージカラーはオレンジですが、建物との統一性を持たせたカラー(紺色:写真参照)のほうが良いかと思っています。(オレンジを使用していただいても結構です)
サイズや表記内容等は「記載項目」をご覧ください。
記載項目
クロベリアルティ株式会社
クロベリーガル事務所またはクロベリーガル行政書士|土地家屋調査士事務所(バランス等考慮し、どちらかを選択)は必須ですが、電話番号は必要ありません。
また、ロゴマークも必須ですが、マークの選択はお任せします。(添付ファイル参照)
また、事業内容については参考に名刺を添付しますが、多くの情報を入れることは望みません。事業所名をクロベリーガル事務所とする場合は、行政書士及び土地家屋調査士を事業内容としていただいても結構です。
寸法につきましては、添付ファイルをご確認ください。

希望イメージ
シンプル 複雑
単色 カラフル
暗い 明るい
日常 高級
遊び心 厳粛
未来的 伝統的
女性的 男性的
希望する色
事務所看板のため、建物と統一性のあるものにしたいです
納品ファイル
• イラストレーター形式 (.ai)
補足説明
事業内容は必ずしも記載しなければならないものではありません。(どちらでもよいです)
■ 選んだ理由

「シンプルでスタイリッシュ」の希望を見事に叶えていただきました。
中でもロゴの配置が絶妙で、色合いも素晴らしかったです。

■ 提案者全員のお礼・コメント

この度は弊社コンペにご参加いただきまして、誠にありがとうございました。
レベルが高く秀逸な作品が多いため選定に悩みましたが、嬉しい悲鳴で選定を楽しませていただきました。
今後も業務拡大を目指しておりますので、折に触れコンペを開催させていただくつもりですので、引き続きよろしくお願いいたします。

```html
<!DOCTYPE html>
<html lang="ja">
<head>
<meta charset="utf-8">
<title>クロベリアルティ株式会社 看板</title>
<link rel="stylesheet" href="https://fonts.googleapis.com/css2?family=Noto+Serif+JP:wght@400;500&display=swap">
<style>
  :root {
    --navy: #0f4468;
    --white: #ffffff;
    --page: #ffffff;
  }
  * { margin: 0; padding: 0; box-sizing: border-box; }
  html, body {
    width: 1200px;
    height: 2520px;
    overflow: hidden;
    background: var(--page);
  }
  .sign {
    position: absolute;
    left: 180px;
    top: 80px;
    width: 840px;
    height: 2320px;
    background: var(--navy);
    color: var(--white);
    font-family: "Noto Serif JP", serif;
  }
  .company-en {
    position: absolute;
    left: 60px;
    top: 100px;
    writing-mode: vertical-rl;
    text-orientation: mixed;
    font-size: 84px;
    font-weight: 400;
    letter-spacing: 0.08em;
    line-height: 1;
  }
  .company-ja {
    position: absolute;
    left: 170px;
    top: 100px;
    writing-mode: vertical-rl;
    font-size: 66px;
    font-weight: 500;
    letter-spacing: 0.02em;
    line-height: 1;
  }
  .services {
    position: absolute;
    left: 260px;
    top: 1175px;
    border-left: 3px solid var(--white);
    list-style: none;
    padding-left: 22px;
  }
  .services li {
    width: 360px;
    font-size: 50px;
    line-height: 1;
    padding: 14px 0 18px;
    border-bottom: 3px solid var(--white);
    letter-spacing: 0.02em;
  }
  .brand {
    position: absolute;
    left: 0;
    top: 1480px;
    width: 840px;
    display: flex;
    flex-direction: column;
    align-items: center;
    gap: 70px;
  }
  .brand-dot {
    width: 180px;
    height: 180px;
    border-radius: 50%;
    background: var(--white);
  }
  .brand-name {
    font-size: 72px;
    font-weight: 400;
    letter-spacing: 0.12em;
    line-height: 1;
  }
</style>
</head>
<body>
  <main class="sign">
    <p class="company-en">KUROBE REALTY</p>
    <h1 class="company-ja">クロベリアルティ株式会社</h1>
    <ul class="services">
      <li>行政書士</li>
      <li>土地家屋調査士</li>
    </ul>
    <div class="brand">
      <span class="brand-dot"></span>
      <span class="brand-name">KUROBE</span>
    </div>
  </main>
</body>
</html>
```